White Paper and One-Page Advertisement for TELVARIS-QP

I need both documents to be better formatted and designed so they look professional, not something someone with mediocre word skills put together. They will go out to 1000s of industry professionals, and they need to look sharp. I need them to have my company's color palate logo, and branding on it similar to how it is now, but better. Please do not change any of the written content, but it can be arranged in any other format you think is better. Smart art and things i've already used can be omitted in favor of better designs. The developer is free to use their creativity. White paper should not be longer than the three pages unless necessary.

Target Market(s)

Life Sciences supply chain professionals

Colors
33b8a4
0592cd
9bcb3c
fbee3e
3277b5

Requirements
Must have
• Must be professional looking and not look like something done in word. Please use the color palate as seen on the documents.
Should not have
• Any changes to the written content.

```html
<!DOCTYPE html>
<html lang="en">
<head>
<meta charset="utf-8">
<title>TELVARIS-QP White Paper</title>
<link rel="stylesheet" href="https://fonts.googleapis.com/css2?family=Exo+2:wght@600;700;800&family=Open+Sans:wght@400;600;700&display=swap">
<style>
:root{
  --teal-dark:#0b3d45;
  --teal:#0f6f62;
  --teal-mid:#33b8a4;
  --green:#1b8a4c;
  --lime:#9bcb3c;
  --lime-bright:#8dc63f;
  --blue:#0592cd;
  --blue-deep:#3277b5;
  --cyan:#3cc3cf;
  --yellow:#fbee3e;
  --ink:#2b2b2b;
  --grey:#6b6b6b;
  --panel:#f2f3f3;
  --stage:#e4e5e6;
}
*{box-sizing:border-box;margin:0;padding:0}
html,body{width:881px;height:1200px;overflow:hidden;background:var(--stage)}
body{position:relative;font-family:"Open Sans",Arial,sans-serif;color:var(--ink)}
.page{position:absolute;width:386px;height:546px;background:#fff;overflow:hidden;box-shadow:0 2px 8px rgba(0,0,0,.25)}
.page--contact{left:52px;top:44px}
.page--cover{left:442px;top:44px}
.page--overview{left:52px;top:608px}
.page--solutions{left:442px;top:608px}
.abs{position:absolute}
.body-text{font-size:4.3px;line-height:1.35;color:#333}
.body-text p{margin-bottom:4px}
.body-text ul{list-style:none;margin:2px 0 4px}
.body-text li{padding-left:7px;position:relative;margin-bottom:1px}
.body-text li:before{content:"o";position:absolute;left:1px;font-size:3.6px}
.sub{font-weight:700;font-size:5px;color:#222;margin:4px 0 2px}
.sub-i{font-style:italic;font-weight:700;font-size:4.6px}
.header-band{position:absolute;left:0;top:0;width:100%;height:56px;background:linear-gradient(90deg,#0a2f3a,#0c4a4c 60%,#0f6757)}
.header-title{position:absolute;color:#fff;font-weight:700;font-size:14.5px;letter-spacing:-.2px}
.brand{position:absolute;display:flex;align-items:center;gap:5px}
.brand-dot{width:22px;height:22px;border-radius:50%;background:var(--green)}
.brand-name{font-family:"Open Sans",Arial,sans-serif;font-weight:700;color:var(--green);letter-spacing:.5px}
.photo{position:absolute;left:192px;width:176px}
.footer-band{position:absolute;left:0;bottom:0;width:100%;height:28px}
.tab{position:absolute;color:#fff;font-weight:700;font-size:11px;padding-left:12px;display:flex;align-items:center}
.stat{position:absolute;top:155px;width:39px;height:64px;background:var(--panel)}
.stat b{display:block;height:14px;color:#fff;font-size:6px;text-align:center;line-height:14px;font-weight:600}
.stat span{display:block;font-size:3.8px;line-height:1.3;padding:3px 3px;color:#333}
.pill{position:absolute;border-radius:9px;color:#fff;font-size:4.2px;text-align:center;font-weight:600}
.btn{position:absolute;width:88px;height:17px;border-radius:2px;color:#fff;font-weight:700;font-size:5px;display:flex;align-items:center;justify-content:center}
.barrier{position:absolute;left:14px;width:170px}
.barrier-bar{height:12px;border-radius:0 6px 6px 0;color:#fff;font-size:5px;font-weight:700;padding-left:5px;display:flex;align-items:center}
.barrier p{font-size:3.9px;line-height:1.3;padding:3px 4px 0;color:#333}
.green-head{color:var(--green);font-weight:700;font-size:11.5px}
</style>
</head>
<body>

<!-- Back page: contact -->
<section class="page page--contact">
  <div class="header-band"></div>
  <svg class="abs" style="left:0;top:0" width="386" height="70" viewBox="0 0 386 70">
    <path d="M150 70 C 240 50, 320 40, 386 30 L386 48 C 320 55, 250 62, 150 70Z" fill="var(--lime)"/>
    <path d="M120 70 C 230 58, 320 50, 386 48 L386 70Z" fill="#fff"/>
  </svg>
  <div class="header-title" style="left:14px;top:26px">How to Find Out More</div>

  <div class="abs body-text" style="left:14px;top:62px;width:170px">
    <p>The exciting new marketplace called TELVARIS-QP is scheduled for initial launch 03 November 2018.</p>
  </div>
  <div class="abs" style="left:14px;top:88px;font-size:6.2px">For more information:</div>
  <ul class="abs" style="left:22px;top:104px;font-size:6.2px;line-height:1.45;list-style:disc;padding-left:8px">
    <li style="padding-left:14px">Email Dale Morrow</li>
    <li style="padding-left:14px">Visit www.telvarisqp.com</li>
    <li style="padding-left:14px">Call 844-555-TVQP</li>
  </ul>
  <div class="abs body-text" style="left:14px;top:148px;width:170px;font-size:3.9px">
    <p>*WE enable a greener, more cost-efficient, and quality driven supply chain through a collaborative life sciences marketplace.</p>
    <p>*WE are an emerging small business with the ultimate goal to educate, inspire, and align Pharma around a new paradigm of waste optimization and sourcing strategies.</p>
    <p>*WE aspire to increase medicine access around the world and decrease Pharma's overall environmental impact.</p>
  </div>
  <div class="abs" style="left:14px;top:226px;font-size:6.2px">Sources</div>
  <div class="abs body-text" style="left:14px;top:240px;width:175px;font-size:3.7px">
    <div class="sub" style="font-size:4.8px;font-weight:600">1. Top 100 Pharma Companies</div>
    <p style="padding-left:8px">• https://industry-rankings.example.org/top-100/league-tables.pdf</p>
    <div class="sub" style="font-size:4.8px;font-weight:600;margin-top:6px">2. 2016 Annual/10K Reports</div>
    <p style="padding-left:8px">• Nineteen leading global drug makers, annual and 10K reports filed for the 2016 fiscal year, summarised for revenue and write-down data.</p>
    <div class="sub" style="font-size:4.8px;font-weight:600;margin-top:6px">3. Total Pharma Revenue 2016</div>
    <p style="padding-left:8px">• http://journal-review.example.org/doi/pdfplus/10.1021/7b00253</p>
    <div class="sub" style="font-size:4.8px;font-weight:600;margin-top:6px">4. Currency Exchange Rates 29 Jan 2018</div>
    <p style="padding-left:8px">• http://fx-tables.example.org/table/?from=USD&amount=1</p>
    <div class="sub" style="font-size:4.8px;font-weight:600;margin-top:6px">5. Pricing Pressure</div>
    <p style="padding-left:8px">• http://med-pricing.example.org/doi/full/10.1056/p160129</p>
  </div>

  <div class="abs" style="left:192px;top:62px;width:176px;text-align:center;color:var(--lime-bright);font-size:4.8px;line-height:1.4;font-weight:600">Every new journey of change and innovation we take is for them...<br>The Patient</div>
  <div class="photo" style="top:84px;height:112px;background:linear-gradient(135deg,#c9bfb4,#e8dcd0 60%,#b7a89a)" role="img" aria-label="Photo of a baby crawling on a soft carpet"></div>
  <div class="photo" style="top:212px;height:116px;background:linear-gradient(135deg,#5f7e96,#c9c2bc 50%,#3f6a8a)" role="img" aria-label="Photo of a smiling elderly woman with glasses"></div>
  <div class="photo" style="top:340px;height:116px;background:linear-gradient(135deg,#3b3a35,#6d5846 55%,#2e302d)" role="img" aria-label="Portrait photo of a young woman in a patterned top"></div>

  <div class="brand" style="left:30px;top:478px">
    <div class="brand-dot"></div>
    <div class="brand-name" style="font-size:14px">TELVARIS-QP</div>
  </div>
  <svg class="footer-band" width="386" height="28" viewBox="0 0 386 28">
    <defs><linearGradient id="fb1" x1="0" x2="1"><stop offset="0" stop-color="#0f6f62"/><stop offset="1" stop-color="#0a3d45"/></linearGradient></defs>
    <path d="M0 12 C120 20, 260 20, 386 6 L386 28 L0 28Z" fill="url(#fb1)"/>
    <path d="M0 10 C120 17, 260 17, 386 3 L386 6 C260 20, 120 20, 0 12Z" fill="var(--lime)"/>
  </svg>
</section>

<!-- Front cover -->
<section class="page page--cover">
  <svg class="abs" style="left:0;top:0" width="386" height="546" viewBox="0 0 386 546">
    <defs>
      <linearGradient id="cv" x1="0" y1="0" x2="1" y2="1"><stop offset="0" stop-color="#0f7c62"/><stop offset=".6" stop-color="#0c5e56"/><stop offset="1" stop-color="#0a3e45"/></linearGradient>
      <linearGradient id="cvl" x1="0" x2="1"><stop offset="0" stop-color="#1b9a52"/><stop offset="1" stop-color="#9bcb3c"/></linearGradient>
      <linearGradient id="cvb" x1="0" x2="1"><stop offset="0" stop-color="#0f6f62"/><stop offset="1" stop-color="#0a3d45"/></linearGradient>
    </defs>
    <rect width="386" height="546" fill="url(#cv)"/>
    <path d="M0 150 C 60 260, 200 330, 386 372 L386 395 C 200 360, 60 300, 0 200Z" fill="url(#cvl)" opacity=".9"/>
    <path d="M0 190 C 70 300, 210 365, 386 395 L386 546 L0 546Z" fill="#fff"/>
    <path d="M0 205 C 80 300, 200 350, 386 365" fill="none" stroke="#d9dedd" stroke-width="2"/>
    <path d="M0 500 C 140 520, 280 520, 386 492 L386 546 L0 546Z" fill="url(#cvb)"/>
    <path d="M0 498 C 140 516, 280 516, 386 488 L386 492 C 280 520, 140 520, 0 500Z" fill="var(--lime)"/>
  </svg>
  <div class="abs" style="right:28px;top:52px;text-align:right;font-family:'Exo 2',sans-serif;font-weight:800;color:var(--lime-bright);font-size:24px;line-height:1.2">CHANGING PHARMA'S<br>PARADIGM OF WASTE</div>
  <div class="abs" style="right:28px;top:138px;text-align:right;color:#fff;font-weight:600;font-size:11.5px;line-height:1.35">How Pharma's Demand Volatility Could<br>Be Costing You Millions in Material<br>Write-downs &amp; Procurement</div>
  <div class="abs" style="right:28px;top:208px;text-align:right;color:#fff;font-weight:600;font-size:11.5px;line-height:1.35">Dale Morrow<br>August 2018</div>
  <div class="brand" style="left:104px;top:418px">
    <div class="brand-dot" style="width:26px;height:26px"></div>
    <div class="brand-name" style="font-size:18px">TELVARIS-QP</div>
  </div>
</section>

<!-- Inside left: overview & baseline -->
<section class="page page--overview">
  <div class="header-band"></div>
  <div class="abs" style="left:186px;top:34px;width:200px;height:22px;background:var(--lime);clip-path:polygon(8% 0,100% 0,100% 100%,0 100%)"></div>
  <div class="header-title" style="left:14px;top:26px">Overview</div>
  <div class="tab" style="left:215px;top:34px;height:22px;font-size:11.5px">Baseline Problem</div>
  <div class="abs" style="left:190px;top:56px;width:196px;height:490px;background:var(--panel)"></div>

  <div class="abs body-text" style="left:12px;top:62px;width:170px;font-size:3.9px">
    <p>Demand volatility is a challenge for every supply chain. It strikes at the end of supply chains causing a "bullwhip effect" that becomes exponentially more impactful further back in the chain. For Pharma, the effect is strongest in manufacturing and procurement, specifically with starting raw materials and consumables. Swings in demand can cripple launches, cause stock-outs, inflate material prices, make lean planning ineffective, and cause significant write-downs of residual/obsolete materials; ultimately inflating CoGS and reducing net income. These swings can also cause inventory costs to inflate, materials to expire or become obsolete, higher disposal fees, and a larger carbon footprint. The yearly financial impacts are staggering considering Pharma's economic footprint. Twenty of Pharma's top 100 companies were sampled using 2015 &amp; 2016 financial figures. Industry estimates for waste include:</p>
  </div>
  <div class="stat" style="left:12px"><b style="background:var(--green)">3.77%</b><span>Avg Raw Material Write-down as a % of net income</span></div>
  <div class="stat" style="left:55px"><b style="background:var(--lime)">$2.7B</b><span>Est Pharma Written Down Inventory in 2016</span></div>
  <div class="stat" style="left:98px"><b style="background:var(--teal-mid)">$2,034</b><span>Est Us Pharma Revenue per 1 Ton Non-MSW Waste</span></div>
  <div class="stat" style="left:141px"><b style="background:var(--cyan)">.01</b><span>Correlation Coefficent of Material Write-downs and firm size</span></div>
  <div class="abs body-text" style="left:12px;top:224px;width:170px;font-size:3.9px">
    <p>What Do These Numbers Mean?</p>
    <ul><li>3.77% is an alarmingly high, and does not include capitalized consumables, equipment disposal, and similar wastes</li></ul>
  </div>
  <div class="pill" style="left:22px;top:246px;width:155px;height:17px;background:var(--teal-dark);padding-top:3px;line-height:1.3">+$5B in net income LS Firm: est $185M in write-downs<br>+$50M in net income LS Firm: est $1.9M in write-downs</div>
  <div class="abs body-text" style="left:12px;top:268px;width:170px;font-size:3.9px">
    <ul>
      <li>$2.7B is likely much lower than the real figure due to capitalizing consumable inventories for launches etc.</li>
      <li>.01 correlation coefficient means this problem does not discriminate based on company size and is ubiquitous in the industry.</li>
      <li>$2,034 to one ton of industrial waste is not progressive.</li>
    </ul>
    <p>Industries have attempted to mitigate the bullwhip effect through many techniques and systems such as ERP, robust forecasting models, demand management, LSS tools, strategic sourcing, etc. However, life science firms still struggle to effectively address this problem as evidenced by the write-down figures. Many non-FDA regulated industries have started utilizing marketplaces and brokerage services to create circular supply chains that optimize waste by connecting buyers and sellers. However, Pharma and life sciences have yet to adopt this waste-centric supply chain and execute it in a manner conducive to the compliance and indemnification requirements of the industry regarding primary and secondary transactions of raw materials, equipment, consumables, spare parts, and collaborative relationships. Finished products such as APIs, intermediates, and devices are out of scope for this supply chain.</p>
    <p><b>A life sciences marketplace and consortium</b> for manufacturers, researchers, and vendors can minimize the aforementioned problems by quickly, innovatively, and transparently exchanging material information in safe and controlled environment ensuring a firm's standards for data integrity, cGMP compliance, contractual indemnification, and financial benefits are met; all by leveraging core auditing skills.</p>
    <p>It is a call to arms among supply chain, procurement, and quality leaders to take part in a more circular, greener, and collaborative supply chain. Time is critical as global competition grows, customer and government emphasis on lowering pricing mounts, and collective pressure on sustainability demands widespread action.</p>
    <p>Let's explore <b>Current</b> and <b>Future State</b> of this industry issue to understand why such a marketplace can begin the much-needed transition for life science companies.</p>
  </div>

  <div class="abs body-text" style="left:198px;top:62px;width:180px;font-size:3.9px">
    <div class="sub">What?</div>
    <ul>
      <li>Disposal of high quality materials, equipment, spare parts</li>
      <li>Single and/or limited sources of supply</li>
      <li>Inability to collaborate with like-minded life sciences firms</li>
      <li>High CoGS due to materials write-downs</li>
      <li>High inventory carrying costs</li>
      <li>Greater business continuity risk</li>
      <li>High disposal costs</li>
      <li>Larger environmental footprint</li>
      <li>Stock-out of materials</li>
    </ul>
    <div class="sub">Who?</div>
    <ul><li>FDA Regulated Industries, Procurement, Quality, Production, and Finance.</li></ul>
    <div class="sub">Where &amp; When</div>
    <ul>
      <li>Commercial &amp; clinical production, R&amp;D, sourcing/purchasing, production planning, quality testing, etc.</li>
      <li>Volatile demand periods, e.g., forecast/product intro growth, decline, seasonality, economic uncertainty, and unforeseen events.</li>
    </ul>
    <div class="sub">How do we know it's there?</div>
    <ul><li>We physically see it taking place, and it's in our data.</li></ul>
    <div class="sub">Triple Bottom Line Impact</div>
    <div class="sub-i">Financial</div>
    <p style="padding-left:14px;margin:1px 0 0"><i>Vendors/ Sellers</i></p>
    <ul style="padding-left:10px"><li>Higher write-downs/offs and 3rd party disposal fees</li></ul>
    <p style="padding-left:14px;margin:0"><i>Buyers</i></p>
    <ul style="padding-left:10px">
      <li>Lost sales – stock-outs</li>
      <li>Inflated market value of materials &amp; supplier expedition fees</li>
      <li>High SS cost due to bullwhip effect</li>
    </ul>
    <p style="padding-left:4px;margin:0"><i>Environment</i></p>
    <ul>
      <li>Greater contribution to global warming through landfill addition, incineration, inactivation, and energy consumption.</li>
      <li>Noncompliance with ISO 14000 &amp; 9000 and B-Corp Status</li>
    </ul>
    <p style="padding-left:4px;margin:0"><i>Society</i></p>
    <ul>
      <li>Lost community trust - high environment and consumer costs</li>
      <li>Less innovation, collaboration, and supply chain optimization</li>
    </ul>
    <div class="sub" style="margin-top:6px">Current State</div>
    <p style="margin:0"><i>External Solutions</i></p>
    <p style="padding-left:6px">Pharma and other FDA industries spend considerable energy on reducing waste. A plethora of techniques are employed to mitigate, prepare for, respond to, and recover from the bullwhip effect, which is one of the leading causes of write-downs. However, such efforts are predicated on:</p>
  </div>
  <div class="btn" style="left:200px;top:427px;background:var(--green)">Forecast Accuracy</div>
  <div class="btn" style="left:292px;top:427px;background:var(--lime)">Supplier Reliability</div>
  <div class="btn" style="left:200px;top:447px;background:#1a9a7e">Process Variability</div>
  <div class="btn" style="left:292px;top:447px;background:var(--teal-mid)">External Environment</div>
  <div class="abs body-text" style="left:198px;top:468px;width:180px;font-size:3.9px">
    <p>While not fruitless, attempts to mitigate the above external influences are extremely unpredictable and have never solved pharma's write-down, inefficiency, stock-out, and environmental problems.</p>
    <div class="sub">Internal Solutions</div>
    <p>The next effort involves reducing obsolescence by reuse of materials within the firm. Typically, interplant demand is the only outlet to optimize surplus earmarked for a reserve/write-down. Even this involves many of the same regulatory compliance, quality, and economic challenges.</p>
    <div class="sub">Environmental Solutions</div>
    <p>FDA industries, like most others, make attempts to reuse, recycle, and convert to energy where applicable.</p>
  </div>
</section>

<!-- Inside right: solutions & paradigm shift -->
<section class="page page--solutions">
  <div class="header-band" style="background:linear-gradient(90deg,#0f6757,#0c4a4c 50%,#0a2f3a)"></div>
  <div class="abs" style="left:0;top:34px;width:196px;height:22px;background:var(--teal-mid);clip-path:polygon(0 0,100% 0,92% 100%,0 100%)"></div>
  <div class="tab" style="left:0;top:34px;height:22px;font-size:11.5px">Undesirable Solutions</div>
  <div class="abs" style="left:0;top:56px;width:192px;height:490px;background:var(--panel)"></div>

  <div class="abs body-text" style="left:14px;top:62px;width:170px;font-size:3.9px">
    <p>Unfortunately, third party disposal (frequently landfill) is typically the first and most popular option as perishable, expiring, and complex materials are generally unable to be reused or recycled. These disposals come in many forms to include responsible landfills, incineration, inactivation, etc.</p>
    <div class="sub">Overall</div>
    <p>Industries spend much capital and resources to reduce write-downs in an environment where the bullwhip effect reigns supreme. Mitigations to this effect are attempted but only partially successful or sustainable.</p>
    <div class="sub" style="font-size:6px;margin-top:6px">Refined Problem</div>
    <p>There is no clear market leader that helps organizations optimize waste, collaborate to reduce it, and market more quality materials to more firms whether for research, manufacturing, or donations. This marketplace must be regulated and all participants properly vetted and authenticated. Accounts must be created to enable companies to post materials and request for information/quotes. Additionally, this marketplace must facilitate collaborative relationships between companies that help them reduce supply chain costs. It must quickly, economically, compliantly, and legally facilitate these exchanges. Lack of this market leader may have enabled the waste problem as seen today.</p>
    <div class="sub">Contemporary Operating Environment</div>
    <ul>
      <li>Constant pressure from global competition, increasing customer and governmental demand on price, more regulatory scrutiny, and a relentless societal pursuit of sustainability are starting to erode what were once high margins for Pharma.</li>
      <li>Regulators are cooperative and open to solutions.</li>
      <li>Exchanges and consortiums are not typically leveraged in Pharma.</li>
      <li>Pharma continues to struggle with the bullwhip effect.</li>
    </ul>
    <div class="sub">Barriers</div>
  </div>
  <div class="barrier" style="top:298px"><div class="barrier-bar" style="background:var(--lime)">Compliance</div><p>It is the responsibility of manufacturers to provide customers/patients with quality, safe, and efficacious products. However, there is a misperception that high quality cGMP compliant materials, parts, and equipment cannot be sourced from aftermarket exchanges and consortiums.</p></div>
  <div class="barrier" style="top:350px"><div class="barrier-bar" style="background:var(--lime-bright)">Liability</div><p>Contractual agreements with suppliers have clauses to resolve issues dealing with poor quality. There is a misperception that these agreements cannot be implemented at both the marketplace and transactional level.</p></div>
  <div class="barrier" style="top:394px"><div class="barrier-bar" style="background:var(--teal)">Economics</div><p>Exchanges can be difficult due to time/effort. A sanctioned marketplace can provide the structure to make it easy.</p></div>
  <div class="barrier" style="top:424px"><div class="barrier-bar" style="background:var(--teal-mid)">Sustainability</div><p>Firms have not discovered how to leverage exchanges to reduce environmental footprint and enable industry certifications as well as community trust.</p></div>
  <div class="barrier" style="top:461px"><div class="barrier-bar" style="background:var(--blue)">Confidence</div><p>Trust is critical to firms. They should know that a marketplace has properly vetted members with KPI data for analysis.</p></div>
  <div class="barrier" style="top:494px"><div class="barrier-bar" style="background:var(--teal)">Confidence</div><p>Exchanges should be fast. An innovative marketplace can ensure quick exchanges.</p></div>

  <div class="abs green-head" style="left:200px;top:64px">Root Cause &amp; Paradigm Shift</div>
  <div class="abs body-text" style="left:200px;top:82px;width:178px;font-size:3.9px">
    <p>Comfort in the status quo has enabled a culture of waste. With life science margins so high, it hasn't been a priority to solve. Additionally, there hasn't been an effective means to deal with waste. This limits the industry's ability to leverage these marketplaces. Finally, misperceived issues or liability and quality have strained innovation; all solvable problems.</p>
    <div class="sub">Future State</div>
    <p>Creation of Private Virtual Life Sciences Multi-Vendor Marketplace &amp; Consortium where researchers, manufacturers, and original end manufacturers can create a simple storefront for their organization and transact materials, equipment, parts, and collaborative relationships in a compliant and professional environment. This marketplace uses a series of software logic that leverages auditing capabilities of buyers and sellers by making FDA required data and documentation visible and subject to ALCOA Plus, thus enabling transactions in a fast and compliant manner. This logic then automates contracts for digital signature in a part 11 compliant package.</p>
    <div class="sub">Benefits</div>
    <ul>
      <li>Avoid write-downs for surplus material/consumable stock</li>
      <li>Continue production when stocked-out of materials</li>
      <li>Reduce purchase price of materials</li>
      <li>Risk pool safety stock to reduce amount required</li>
      <li>Allow for leaner planning in that stock-outs can be addressed</li>
      <li>Allow for more responsive planning with an outlet to sell SS</li>
      <li>Reduce supplier audit resources and costs</li>
      <li>Reduce environment footprint by avoiding disposal fees</li>
    </ul>
  </div>
  <svg class="abs" style="left:196px;top:286px" width="190" height="120" viewBox="0 0 190 120">
    <path d="M18 30 C 20 10, 50 4, 70 14 C 85 0, 120 2, 130 16 C 150 6, 180 18, 176 38 C 190 52, 184 80, 166 86 C 168 106, 140 116, 120 106 C 104 120, 70 118, 60 104 C 36 114, 10 100, 14 82 C 0 70, 2 44, 18 30Z" fill="var(--cyan)"/>
  </svg>
  <div class="abs" style="left:222px;top:306px;width:140px;color:#fff;font-size:5px;line-height:1.35;font-weight:600">
    <div style="margin-bottom:5px">Vision</div>
    <div style="margin-bottom:6px">1. A collaborative and compliant multi-vendor marketplace is part of Pharma's normal operating practices</div>
    <div style="margin-bottom:6px">2. Waste is not tolerated in the life sciences industry</div>
    <div>3. There is always a compliant outlet</div>
  </div>
  <div class="abs body-text" style="left:200px;top:440px;width:178px;font-size:3.9px">
    <div class="sub">How to Implement</div>
    <p>Application of the following guidance, regulations, and bodies will drive exchange process and design:</p>
    <ul>
      <li>ICH Q7 (International harmonized cGMP standards)</li>
      <li>CFR Title 21 (US cGMP standards)</li>
      <li>Data Integrity Draft Guidance by FDA (good doc practices)</li>
      <li>WHO GMP for Pharmaceutical Products (World Health Organizations cGMP standards)</li>
      <li>APIC - Good Manufacturing Practices in Active Pharmaceutical Ingredients Development, 1999.</li>
      <li>APIC Supplier Qualification and Management Guidelines</li>
    </ul>
    <div class="sub-i">Data Integrity</div>
    <p>Data integrity will drive how the exchange operates. All parties are encouraged to use the FDA's ALCOA-Plus system to review documents associated with transactions. This enables buyers' standards of data integrity and cGMP quality compliance to be adhered.</p>
  </div>
</section>

</body>
</html>
```